Sumvane financial services stationery design

We need business stationery designed with letterheads, business cards, with compliments and envelope for a business that offers tax and accounting services

Designs look the same

Target Market(s)

Small to medium businesses, individuals, Self managed superfunds

Industry/Entity Type

Business

Font styles to use
Serif
Other font styles liked:
• Atlanta

Colors
32a6d6
3277b5

Requirements
Must have
• Logo incorporated with all my stationery
• professional
Should not have
• Lots of colours
• Busy

```html
<!DOCTYPE html>
<html lang="en">
<head>
<meta charset="utf-8">
<title>Sumvane Financial Services – Stationery</title>
<link rel="stylesheet" href="https://fonts.googleapis.com/css2?family=Arimo:wght@400;700&family=Montserrat:wght@500;600&display=swap">
<style>
  :root {
    --backdrop: #e4e5e7;
    --paper: #ffffff;
    --paper-shade: #f4f5f7;
    --brand-blue: #3277b5;
    --brand-deep: #3a64b0;
    --brand-light: #5b9bd8;
    --card-blue: #4472b8;
    --ink: #222428;
    --ink-soft: #55585e;
    --logo-ink: #3b3d42;
  }
  * { box-sizing: border-box; margin: 0; padding: 0; }
  html, body { width: 1200px; height: 960px; overflow: hidden; }
  body {
    background: var(--backdrop);
    font-family: "Arimo", Arial, sans-serif;
    color: var(--ink);
    position: relative;
  }
  .sheet { position: absolute; background: var(--paper); box-shadow: 0 2px 10px rgba(0,0,0,.12); }

  /* Brand name block: one font, one weight, one colour */
  .brand { display: flex; align-items: center; gap: 10px; white-space: nowrap; }
  .brand__square { width: 14px; height: 14px; background: var(--brand-blue); flex: none; }
  .brand__name {
    font-family: "Montserrat", Arial, sans-serif; font-weight: 600;
    color: var(--logo-ink); font-size: 24px; line-height: 1;
  }

  /* Letterhead */
  .letterhead { left: 40px; top: 40px; width: 610px; height: 870px; }
  .letterhead .brand { position: absolute; left: 56px; top: 70px; }
  .letter { position: absolute; left: 70px; top: 190px; width: 470px; font-size: 10.5px; line-height: 1.45; }
  .letter__salutation { font-weight: 700; font-size: 13px; margin-bottom: 14px; }
  .letter p { margin-bottom: 10px; }
  .letter__closing { margin-top: 26px; font-size: 12px; }
  .letter__signature { width: 60px; height: 22px; margin: 8px 0 6px; background: #eef0f4; border-radius: 3px; }
  .letter__name { font-family: "Montserrat", sans-serif; font-weight: 600; font-size: 13px; }
  .letter__role { font-weight: 700; font-size: 9px; }
  .letterhead__footer {
    position: absolute; left: 56px; right: 40px; bottom: 34px;
    font-family: "Montserrat", sans-serif; font-weight: 600; font-size: 10.5px; color: var(--ink-soft);
    display: flex; gap: 10px; align-items: center; white-space: nowrap;
  }
  .footer__divider { width: 2px; height: 12px; background: var(--brand-blue); flex: none; }
  .letterhead__band { position: absolute; left: 0; right: 0; bottom: 0; height: 10px; display: flex; }
  .band__main { flex: 0 0 75%; background: var(--brand-deep); }
  .band__accent { flex: 1; background: var(--brand-light); margin-left: 3px; }

  /* Business card front */
  .card-front { left: 700px; top: 40px; width: 420px; height: 230px; background: var(--card-blue); }
  .card-front .brand { position: absolute; left: 40px; top: 104px; }
  .card-front .brand__square { background: #ffffff; }
  .card-front .brand__name { color: #ffffff; font-size: 20px; }

  /* Business card back */
  .card-back { left: 700px; top: 300px; width: 420px; height: 230px; }
  .card-back__accent { position: absolute; left: 30px; top: 30px; width: 3px; height: 34px; background: var(--brand-blue); }
  .card-back__name { position: absolute; left: 42px; top: 30px; font-family: "Montserrat", sans-serif; font-weight: 600; font-size: 15px; color: var(--brand-blue); letter-spacing: .5px; }
  .card-back__role { position: absolute; left: 42px; top: 51px; font-size: 8px; font-weight: 700; letter-spacing: 1px; color: var(--ink-soft); }
  .card-back__address { position: absolute; left: 42px; top: 84px; font-size: 9px; line-height: 1.35; color: var(--ink-soft); }
  .contact-list { position: absolute; left: 30px; top: 122px; list-style: none; font-size: 9px; color: var(--ink-soft); }
  .contact-list li { display: flex; align-items: center; gap: 6px; margin-bottom: 4px; }
  .contact-list svg { width: 9px; height: 9px; fill: var(--brand-blue); }
  .card-back .brand { position: absolute; right: 28px; bottom: 34px; gap: 8px; }
  .card-back .brand__name { font-size: 13px; }
  .card-back .brand__square { width: 10px; height: 10px; }

  /* Envelope */
  .envelope { left: 700px; top: 560px; width: 420px; height: 350px; background: var(--paper-shade); }
  .envelope .brand { position: absolute; left: 40px; top: 50px; }
  .envelope .brand__name { font-size: 20px; }
</style>
</head>
<body>

  <section class="sheet letterhead" aria-label="Letterhead">
    <div class="brand">
      <span class="brand__square"></span>
      <span class="brand__name">Sumvane Financial Services</span>
    </div>

    <article class="letter">
      <p class="letter__salutation">Dear Mr. Holloway</p>
      <p>Thank you for choosing us to look after your tax and accounting affairs this year. We have reviewed the documents you sent and prepared a summary of the items that need your attention before the end of the financial year, including deductions, records and lodgement dates.</p>
      <p>Our team will contact you next week to arrange a short meeting at a time that suits you.</p>
      <p>Please keep copies of receipts, bank statements and invoices together so we can finish your return quickly. If your circumstances have changed, such as a new property, business or superannuation fund, let us know so we can adjust our advice.</p>
      <p>We appreciate your trust and look forward to working with you again. Should you have any questions in the meantime, please call our office or send us an email and a member of our team will respond promptly.</p>
      <div class="letter__closing">Sincerely Yours,</div>
      <div class="letter__signature" role="img" aria-label="Handwritten signature"></div>
      <div class="letter__name">YOUR NAME</div>
      <div class="letter__role">Executive Director</div>
    </article>

    <footer class="letterhead__footer">
      <span>Level 4, 18 Alder Lane, Brookfield 4410</span>
      <span class="footer__divider"></span>
      <span>www.sumvaneservices.com</span>
      <span class="footer__divider"></span>
      <span>(07) 5550 1842</span>
    </footer>
    <div class="letterhead__band"><span class="band__main"></span><span class="band__accent"></span></div>
  </section>

  <section class="sheet card-front" aria-label="Business card front">
    <div class="brand">
      <span class="brand__square"></span>
      <span class="brand__name">Sumvane Financial Services</span>
    </div>
  </section>

  <section class="sheet card-back" aria-label="Business card back">
    <span class="card-back__accent"></span>
    <div class="card-back__name">HOLLOWAY</div>
    <div class="card-back__role">DIRECTOR</div>
    <div class="card-back__address">Level 4, 18 Alder Lane<br>Brookfield 4410</div>
    <ul class="contact-list">
      <li><svg viewBox="0 0 10 10"><path d="M2 0.5 L4 2.5 L3 3.8 Q4.5 6 6.2 7 L7.5 6 L9.5 8 L8 9.5 Q3 9 0.5 2 Z"/></svg>(07) 5550 1842</li>
      <li><svg viewBox="0 0 10 10"><rect x="1" y="2" width="8" height="6" rx="1"/></svg>(07) 5550 1843</li>
      <li><svg viewBox="0 0 10 10"><path d="M0.5 2 H9.5 V8 H0.5 Z"/></svg>info@sumvaneservices.com</li>
      <li><svg viewBox="0 0 10 10"><circle cx="5" cy="5" r="4.5"/></svg>www.sumvaneservices.com</li>
    </ul>
    <div class="brand">
      <span class="brand__square"></span>
      <span class="brand__name">Sumvane Financial Services</span>
    </div>
  </section>

  <section class="sheet envelope" aria-label="Envelope">
    <div class="brand">
      <span class="brand__square"></span>
      <span class="brand__name">Sumvane Financial Services</span>
    </div>
  </section>

</body>
</html>
```